Landing page for a sports website

we have a sports tracking and management website and require a web site.
the site should have the ability to have 2 options for selection the first being a competitions portal the other a club portal there should be a about us page and a contact us page
the site should be dynamic and vibrant and be easily recognisable as a multiple sports page
we also have www.tilvoshelf.net and would like it to compliment that site
i would like to have some form of animation regarding sports occur when you click the login option if that is possible
the site is www.drqplays.net and I have attached the logo in both 3d and standard
we also require a design several templates for information pages please see www.lunaforge.net as an example of how it should look but with a sports theme
Target Market(s)
This will be used for primarily team based sports
Industry/Entity Type
Management
Number of Pages Required
3 page
Requirements
Must have
- the ability to change the logo and names of the site
- i.e. from drqplays to drqcampus at a later date

```html
<!DOCTYPE html>
<html lang="en">
<head>
<meta charset="utf-8">
<title>DRQ Plays</title>
<link rel="stylesheet" href="https://fonts.googleapis.com/css2?family=Open+Sans:wght@400;700&family=Roboto+Slab:wght@400;500;700&display=block">
<style>
  :root {
    --header-top: #2c2c2c;
    --header-bottom: #0d0d0d;
    --stage-top: #1a1a1a;
    --stage-mid: #0b0b0b;
    --stage-bottom: #020202;
    --brand-blue: #3fb0d8;
    --nav-text: #a6a6a6;
    --nav-accent: #e07b2c;
    --divider: #8a8a8a;
    --button-top: #d9584c;
    --button-mid: #cc3a2f;
    --button-bottom: #9e2a21;
    --button-text: #ffffff;
    --footer-band: #b02e27;
  }
  * { box-sizing: border-box; margin: 0; padding: 0; }
  html, body { width: 1200px; height: 1000px; overflow: hidden; background: #000; }
  .page { position: relative; width: 1200px; height: 1000px; font-family: "Open Sans", sans-serif; }

  .site-header {
    position: absolute; left: 0; top: 0; width: 1200px; height: 155px;
    background: linear-gradient(to bottom, var(--header-top), var(--header-bottom));
  }
  .brand {
    position: absolute; left: 185px; top: 48px;
    display: flex; align-items: center; gap: 12px;
    font-family: "Open Sans", sans-serif; font-weight: 700; font-size: 44px; line-height: 56px;
    color: var(--brand-blue); letter-spacing: 1px;
  }
  .brand-mark { width: 22px; height: 22px; background: var(--brand-blue); }

  .main-nav { position: absolute; left: 584px; top: 63px; display: flex; height: 30px; }
  .nav-item {
    display: flex; align-items: center; height: 30px; line-height: 30px;
    border-left: 1px solid var(--divider);
    font-size: 15px; color: var(--nav-text); letter-spacing: 0.4px;
  }
  .nav-item:first-child { border-left-color: var(--nav-accent); }
  .nav-about { width: 209px; padding-left: 37px; }
  .nav-contact { width: 134px; padding-left: 34px; }
  .nav-more { padding-left: 39px; color: var(--nav-accent); gap: 8px; }
  .nav-more svg { width: 12px; height: 10px; }

  .stage {
    position: absolute; left: 0; top: 155px; width: 1200px; height: 800px;
    background:
      radial-gradient(ellipse 75% 55% at 50% 18%, var(--stage-top), var(--stage-mid) 55%, var(--stage-bottom) 90%);
  }
  .header-edge {
    position: absolute; left: 0; top: 155px; width: 1200px; height: 22px;
    background: linear-gradient(to bottom, #3a3a3a, rgba(20,20,20,0));
  }

  .portal-button {
    position: absolute; top: 443px; width: 282px; height: 72px;
    display: flex; align-items: center; justify-content: center;
    background: linear-gradient(to bottom, var(--button-top), var(--button-mid) 50%, var(--button-bottom));
    font-family: "Roboto Slab", "Rockwell", "Courier New", serif; font-weight: 500; font-size: 24px;
    color: var(--button-text); letter-spacing: 1px; text-decoration: none;
  }
  .portal-competitions { left: 283px; }
  .portal-club { left: 652px; }

  .site-footer {
    position: absolute; left: 0; top: 955px; width: 1200px; height: 45px;
    background: var(--footer-band);
  }
</style>
</head>
<body>
<div class="page">
  <div class="stage" role="img" aria-label="Dark hexagonal carbon texture backdrop"></div>
  <div class="header-edge"></div>

  <header class="site-header">
    <div class="brand"><span class="brand-mark"></span>DRQ Plays</div>
    <nav class="main-nav">
      <span class="nav-item nav-about">About DRQ Plays</span>
      <span class="nav-item nav-contact">Contact</span>
      <span class="nav-item nav-more">More
        <svg viewBox="0 0 12 10"><polygon points="0,0 12,0 6,10" fill="#e07b2c"/></svg>
      </span>
    </nav>
  </header>

  <a class="portal-button portal-competitions">COMPETITIONS</a>
  <a class="portal-button portal-club">CLUB</a>

  <footer class="site-footer"></footer>
</div>
</body>
</html>
```